2 Business Card Designs

Need two business cards designed:
1) for lumora films (wedding video) website is lumorafilms.com.au
2) for lumora films (corporate video) website is lumorafilms.net.au

I am looking for something simple, no fancy shapes etc. Just elegant, simple and classy.

Both companies are video companies, one specialising in weddings the other corporate videos. Neither card needs to have any pics of video or camera related images. Please use same colour schemes as respective websites.

Logo is the same but can change colour.

Industry/Entity Type

Camera

Requirements
Must have
• Logo should be either all white or a colour to match websites
Should not have
• swirls, flowers, shapes, etc.

```html
<!DOCTYPE html>
<html lang="en">
<head>
<meta charset="utf-8">
<title>lumora films — business cards</title>
<link rel="stylesheet" href="https://fonts.googleapis.com/css2?family=Questrial&display=swap">
<style>
  :root {
    --backdrop: #d8913b;
    --card: #dfe1cb;
    --band: #676859;
    --ink: #676859;
    --ink-soft: #7a7b6c;
    --band-text: #f2f3e6;
  }
  * { margin: 0; padding: 0; box-sizing: border-box; }
  html, body {
    width: 1200px; height: 923px; overflow: hidden;
    background: var(--backdrop);
    font-family: "Questrial", Helvetica, Arial, sans-serif;
  }
  .canvas { position: relative; width: 1200px; height: 923px; }

  .card {
    position: absolute;
    background: var(--card);
    width: 555px; height: 369px;
  }
  .card--wedding   { left: 106px; top: 41px; }
  .card--corporate { left: 508px; top: 484px; }

  .footer-band {
    position: absolute; left: 0; right: 0;
    top: 313px; height: 36px;
    background: var(--band);
    display: flex; align-items: center; justify-content: center;
    color: var(--band-text);
    font-size: 16px; letter-spacing: 1.2px;
  }

  .wordmark {
    position: absolute; left: 0; right: 0; top: 120px;
    text-align: center;
    color: var(--ink);
    font-size: 36px; font-weight: 400; line-height: 1;
    letter-spacing: 1px;
  }
  .services {
    color: var(--ink-soft);
    font-size: 12px; letter-spacing: 0.6px;
    white-space: nowrap;
  }
  .services .sep { margin: 0 16px; }
  .card--wedding .services {
    position: absolute; left: 0; right: 0; top: 189px; text-align: center;
  }

  .holder-name {
    position: absolute; left: 200px; top: 54px;
    color: var(--ink);
    font-size: 27px; font-weight: 400; letter-spacing: 1px;
  }
  .service-band {
    position: absolute; right: 0; top: 95px;
    width: 381px; height: 31px;
    background: var(--band);
    display: flex; align-items: center; justify-content: center;
  }
  .service-band .services { color: var(--band-text); font-size: 12px; }
  .service-band .sep { margin: 0 12px; }

  .contact {
    position: absolute; left: 311px; top: 148px;
    color: var(--ink);
    font-size: 15px; letter-spacing: 0.6px;
    line-height: 23px;
  }
  .contact-row { display: flex; }
  .contact-label { width: 81px; }
  .contact-email {
    position: absolute; right: 28px; top: 221px;
    color: var(--ink);
    font-size: 15px; letter-spacing: 0.4px;
  }
</style>
</head>
<body>
<main class="canvas">

  <section class="card card--wedding" aria-label="Wedding video card">
    <div class="wordmark">lumora films</div>
    <p class="services">Wedding<span class="sep">|</span>Event<span class="sep">|</span>Corporate<span class="sep">|</span>Commercial</p>
    <div class="footer-band">www.lumorafilms.com.au</div>
  </section>

  <section class="card card--corporate" aria-label="Corporate video card">
    <h1 class="holder-name">Marcus</h1>
    <div class="service-band">
      <p class="services">Wedding<span class="sep">|</span>Event<span class="sep">|</span>Corporate<span class="sep">|</span>Commercial</p>
    </div>
    <div class="contact">
      <div class="contact-row"><span class="contact-label">Office:</span><span>61 2 5550 1274</span></div>
      <div class="contact-row"><span class="contact-label">Call:</span><span>61 2 5550 1274</span></div>
      <div class="contact-row"><span class="contact-label">Fax:</span><span>61 2 5550 1274</span></div>
    </div>
    <p class="contact-email">marcus@lumorafilms.net.au</p>
    <div class="footer-band">www.lumorafilms.net.au</div>
  </section>

</main>
</body>
</html>
```